DERMATOLOGY SERVICES ADDING CARE FOR sKIN, HAIR AND NAILS

postcard TO BE DISTRIBUTED TO RURAL COMMUNITY. medical CLINIC EXPANDING AND ADDING DERMATOLOGIST. TREATMENT OF skin PROBLEMS LIKE RASHES, SABIES, SKIN CANCERS, ROSACEA, PSORIASIS, ECZEMA, WOUND CARE, ACNE, ANTI-AGING AND OTHER BREAKDOWN OF SKIN.
SERVICES INCLUDED PLEASE SEE ATTACHED DOCUMENT
Updates

Project Deadline Extended
Reason: The designs we got few designers that sent designs and they are not what we want. We need to have more time

Target Market(s)

rural COMMUNITY

Industry/Entity Type

Medical

Font styles to use
Other font styles liked:
• LET DESIGNER CHOOSE

Requirements
Must have
• SKIN PROBLEMS AND DISORDERS MENTIONED IN THE ATTACHED FILES
• MEDICAL PROFESSION
• ADDRESS PHONE NUMBERS
• 482 N Larkin Avenue Wauchula, Florida 33870
• phone # 863-555-0182
• Marlow Tenbury Inc expanding its services
• mOST INSURANCE ACCEPTED INCLUDING MEDICARE
Nice to have
• ADD A LOGO
Should not have
• This is a US postcard to be left in restaurants, doctors offices RV park. No stamp or address line in the back

```html
<!DOCTYPE html>
<html lang="en">
<head>
<meta charset="utf-8">
<title>Dermatology Postcard</title>
<link href="https://fonts.googleapis.com/css2?family=Roboto+Condensed:ital,wght@0,400;0,700;1,700&family=Tinos&display=swap" rel="stylesheet">
<style>
  :root {
    --backdrop: #4a2e22;
    --blue: #1f4f9e;
    --blue-dark: #163a78;
    --red: #c8161d;
    --red-dark: #a10f15;
    --yellow: #ffd200;
    --white: #ffffff;
    --ink: #333333;
    --grey: #e0e0e0;
    --serif-blue: #2a5fa8;
  }
  * { box-sizing: border-box; margin: 0; padding: 0; }
  html, body { width: 831px; height: 1200px; overflow: hidden; }
  body {
    background: var(--backdrop);
    font-family: "Roboto Condensed", Arial, sans-serif;
    position: relative;
  }
  .card {
    position: absolute;
    left: 78px;
    width: 675px;
    height: 540px;
    background: var(--white);
    overflow: hidden;
  }
  .front { top: 28px; }
  .back { top: 620px; }

  /* Front */
  .front .hero-photo {
    position: absolute; right: 0; top: 120px; width: 400px; height: 350px;
    background: radial-gradient(ellipse at 60% 45%, #f4dccb 0%, #eccfbd 35%, #f3f1f0 75%);
  }
  .front .header {
    position: absolute; left: 0; top: 0; width: 100%; height: 110px;
    background: linear-gradient(180deg, #2a63b8, var(--blue-dark));
    color: var(--white); font-weight: 700; font-size: 31px; line-height: 36px;
    padding: 18px 0 0 32px; text-transform: uppercase;
  }
  .front .treatment-bar {
    position: absolute; left: 0; top: 112px; width: 462px; height: 46px;
    background: var(--red); color: var(--yellow); font-weight: 700;
    font-size: 24px; line-height: 46px; padding-left: 32px; white-space: nowrap;
  }
  .front .expanding-badge {
    position: absolute; right: 12px; top: 108px; width: 190px; height: 92px;
    background: var(--yellow); color: var(--red-dark); font-weight: 700;
    font-size: 20px; line-height: 25px; text-align: center; padding-top: 9px;
  }
  .front .location-bar {
    position: absolute; left: 0; top: 162px; width: 300px; height: 28px;
    background: var(--blue); color: var(--white); font-weight: 700;
    font-size: 15px; line-height: 28px; padding-left: 32px; white-space: nowrap;
  }
  .services {
    position: absolute; left: 40px; top: 214px; list-style: none;
    color: var(--ink); font-size: 21px; line-height: 24px;
  }
  .services li { position: relative; padding-left: 32px; margin-bottom: 8px; width: 250px; }
  .services li::before {
    content: ""; position: absolute; left: 0; top: 4px; width: 16px; height: 16px;
    border-radius: 50%; background: var(--red);
  }
  .front .insurance {
    position: absolute; left: 0; top: 442px; width: 230px; height: 98px;
    background: var(--red); color: var(--yellow); font-weight: 700;
    font-size: 18px; line-height: 23px; padding: 20px 0 0 30px; z-index: 2;
  }
  .front .call-bar {
    position: absolute; left: 0; top: 470px; width: 100%; height: 70px;
    background: linear-gradient(180deg, #2a63b8, var(--blue-dark));
    color: var(--white); font-style: italic; font-weight: 700; font-size: 30px;
    line-height: 70px; text-align: right; padding-right: 40px;
  }

  /* Back */
  .back .red-panel {
    position: absolute; left: 0; top: 0; width: 338px; height: 100%;
    background: linear-gradient(180deg, var(--red), var(--red-dark));
    color: var(--white); padding: 28px 0 0 28px;
  }
  .back h2 { color: var(--yellow); font-size: 32px; line-height: 37px; font-weight: 700; }
  .back .treat-lead { font-size: 24px; font-weight: 700; margin-top: 18px; }
  .conditions {
    list-style: none; display: grid; grid-template-columns: 132px 150px;
    column-gap: 16px; row-gap: 6px; margin-top: 10px;
    color: var(--yellow); font-size: 16px; font-weight: 700; white-space: nowrap;
  }
  .conditions li { position: relative; padding-left: 18px; }
  .conditions li::before {
    content: ""; position: absolute; left: 0; top: 6px; width: 9px; height: 9px;
    background: var(--yellow); border-radius: 50%;
  }
  .back .map-area {
    position: absolute; left: 28px; top: 272px; width: 210px; height: 140px;
    background: linear-gradient(135deg, #e8eee6, #d4dfe6);
  }
  .back .address { position: absolute; left: 28px; top: 448px; font-size: 15px; white-space: nowrap; }
  .back .phone { position: absolute; left: 28px; top: 476px; font-size: 23px; font-weight: 700; color: var(--yellow); white-space: nowrap; }
  .back .tagline {
    position: absolute; left: 378px; top: 165px; width: 260px;
    font-family: "Tinos", Georgia, serif; color: var(--serif-blue);
    font-size: 21px; line-height: 30px; text-align: center;
  }
  .back .tagline p + p { margin-top: 28px; }
  .back .footer-band {
    position: absolute; left: 338px; bottom: 0; width: 337px; height: 34px; background: var(--grey);
  }
</style>
</head>
<body>
  <section class="card front">
    <div class="hero-photo" role="img" aria-label="Portrait photo of a woman with clear skin"></div>
    <div class="header">Medical Clinic Expanding and Adding<br>Dermatologist Service</div>
    <div class="treatment-bar">Treatment of Skin Problems like Rashes</div>
    <div class="expanding-badge">Marlow Tenbury Inc<br>Expanding<br>Its Services</div>
    <div class="location-bar">Dermatologist now in Wauchula, Florida</div>
    <ul class="services">
      <li>Skin exams</li>
      <li>Skin Disorders</li>
      <li>Skin Biopsies</li>
      <li>Mole and Skin Tag removal</li>
      <li>Treatment of various skin, hair and nail disease</li>
    </ul>
    <div class="insurance">MOST INSURANCE<br>ACCEPTED INCLUDING<br>MEDICARE</div>
    <div class="call-bar">Call us today : (863) 555-0182</div>
  </section>

  <section class="card back">
    <div class="red-panel">
      <h2>Dermatologist now<br>in Wauchula, Florida</h2>
      <p class="treat-lead">Treat skin problems like</p>
      <ul class="conditions">
        <li>Skin Cancers</li><li>Rosacea</li>
        <li>Psoriasis</li><li>Eczema</li>
        <li>Wound care</li><li>Other Breakdowns</li>
      </ul>
      <div class="map-area" role="img" aria-label="Street map showing the clinic location"></div>
      <p class="address">482 N Larkin Avenue Wauchula, Florida 33870</p>
      <p class="phone">Call us today : (863) 555-0182</p>
    </div>
    <div class="tagline">
      <p>CARE IN YOUR<br>COMMUNITY</p>
      <p>MEDICAL PROFESSION</p>
    </div>
    <div class="footer-band"></div>
  </section>
</body>
</html>
```